Business card design for a content marketing agency

Need a business card design suitable for a digital marketing agency. Needs to be a bold and creative, high quality design that exudes expertise and professionalism, and instills in prospective new customers a sense of confidence that we are the right company to do business with. Specifications must meet PrintNorvo requirement for extra thick matte stock. Needs to incorporate logo, tagline, name, title, website url, address, city, state, zip code, and mobile number.. I spec'd s single side design but I'm to a double sided design if it's strong and compelling. I like the use of icons associated with contact info, but it's not a requirement. Mostly, the design needs to command attention because it's so good or unusual. I have all kinds of files in large thru small sizes in jpg andpgn. pick from what you need, and let me know if you have questions.

Target Market(s)

CEO, Mktg VP's and small to medium size tech and prof'l service businesses

Industry/Entity Type

Marketing

Contact Information for Business Card

Perry Lindqvist
Chief Executive Officer
418 Wexcombe Lane
Brinmoor, NH 03999
perry@quelmarketing.example
www.quelmarketing.example
978-555-2716

Font styles to use
Sans Serif

Colors
0692cd
9bcb3c

Requirements
Must have
• Tagline is "Marketing Built On Client Trust".
• Needs to be a bold and creative, high quality design that exudes expertise and professionalism, and instills in prospective new customers a sense of confidence that we are the right company to do business with. Specifications must meet PrintNorvo requirement for extra thick matte stock. Needs to incorporate logo, tagline, name, title, website url, address, city, state, zip code, and mobile number..
Nice to have
• I spec'd s single side design but I'm open to a double sided design if it's strong and compelling. I like the use of icons associated with contact info, but it's not a requirement.
Should not have
• Chose colors that are the same and/or compatible with colors in the logo

```html
<!DOCTYPE html>
<html lang="en">
<head>
<meta charset="UTF-8">
<title>Quel Marketing — Business Card</title>
<link rel="stylesheet" href="https://fonts.googleapis.com/css2?family=Lato:wght@400;700&display=swap">
<style>
  :root {
    --stage: #2e2e2e;
    --card: #f7f7f7;
    --brand-blue: #0d6fb0;
    --brand-blue-light: #2a8fd0;
    --ink: #111111;
    --white: #ffffff;
  }
  * { box-sizing: border-box; margin: 0; padding: 0; }
  html, body {
    width: 1200px; height: 997px; overflow: hidden;
    background: var(--stage);
    font-family: "Lato", Arial, sans-serif;
  }
  .canvas { position: relative; width: 1200px; height: 997px; }
  .card {
    position: absolute; width: 600px; height: 343px;
    background: var(--card); border-radius: 18px; overflow: hidden;
    box-shadow: 0 12px 30px rgba(0,0,0,.45);
  }
  .card--front { left: 80px; top: 90px; }
  .card--back { left: 520px; top: 540px; }
  .card__shapes { position: absolute; inset: 0; }

  .brand { display: flex; align-items: center; gap: 12px; }
  .brand__dot { width: 22px; height: 22px; border-radius: 50%; background: var(--brand-blue); }
  .brand__name { font-weight: 700; color: var(--brand-blue); letter-spacing: .2px; white-space: nowrap; }

  .front__brand { position: absolute; left: 56px; top: 128px; }
  .front__brand .brand__name { font-size: 36px; }
  .front__tagline {
    position: absolute; left: 90px; top: 178px;
    font-size: 16px; color: var(--brand-blue-light); letter-spacing: .5px; white-space: nowrap;
  }
  .front__url { font-family: "Lato", Arial, sans-serif; font-size: 15px; fill: var(--white); letter-spacing: .6px; }

  .back__brand { position: absolute; right: 36px; top: 52px; }
  .back__brand .brand__name { font-size: 26px; }
  .back__person { position: absolute; left: 38px; top: 120px; }
  .back__name { font-size: 24px; font-weight: 700; color: var(--brand-blue); letter-spacing: .6px; text-transform: uppercase; }
  .back__title { font-size: 17px; color: var(--ink); margin-top: 2px; }

  .contact { position: absolute; left: 34px; top: 242px; list-style: none; color: var(--white); font-size: 16px; }
  .contact__item { display: flex; align-items: flex-start; gap: 22px; line-height: 21px; margin-bottom: 3px; }
  .contact__icon { width: 16px; height: 16px; margin-top: 3px; flex: none; }
</style>
</head>
<body>
<main class="canvas">

  <section class="card card--front" aria-label="Card front">
    <svg class="card__shapes" width="600" height="343" viewBox="0 0 600 343">
      <path d="M380 343 Q520 245 600 24 L600 50 Q538 258 418 343 Z" fill="var(--ink)"/>
      <path d="M430 343 Q548 262 600 64 L600 343 Z" fill="var(--brand-blue)"/>
      <path id="url-track" d="M470 334 Q556 268 590 120" fill="none"/>
      <text class="front__url"><textPath href="#url-track" startOffset="6%">www.quelmarketing.example</textPath></text>
    </svg>
    <div class="brand front__brand">
      <span class="brand__dot"></span>
      <span class="brand__name">Quel Marketing</span>
    </div>
    <p class="front__tagline">Marketing Built On Client Trust</p>
  </section>

  <section class="card card--back" aria-label="Card back">
    <svg class="card__shapes" width="600" height="343" viewBox="0 0 600 343">
      <path d="M0 224 Q300 150 600 176 L600 184 Q300 168 0 244 Z" fill="var(--ink)"/>
      <path d="M0 244 Q300 172 600 194 L600 343 L0 343 Z" fill="var(--brand-blue)"/>
    </svg>
    <div class="brand back__brand">
      <span class="brand__dot"></span>
      <span class="brand__name">Quel Marketing</span>
    </div>
    <div class="back__person">
      <p class="back__name">Perry Lindqvist</p>
      <p class="back__title">Chief Executive Officer</p>
    </div>
    <ul class="contact">
      <li class="contact__item">
        <svg class="contact__icon" viewBox="0 0 16 16"><rect x="3.5" y="1" width="9" height="14" rx="1.5" fill="none" stroke="var(--ink)" stroke-width="1.8"/></svg>
        <span>978-555-2716</span>
      </li>
      <li class="contact__item">
        <svg class="contact__icon" viewBox="0 0 16 16"><rect x="1" y="3" width="14" height="10" rx="1" fill="var(--ink)"/><path d="M1.5 3.8 L8 9 L14.5 3.8" fill="none" stroke="var(--brand-blue)" stroke-width="1.2"/></svg>
        <span>perry@quelmarketing.example</span>
      </li>
      <li class="contact__item">
        <svg class="contact__icon" viewBox="0 0 16 16"><path d="M8 1 C4.8 1 3 3.3 3 6 C3 9.5 8 15 8 15 C8 15 13 9.5 13 6 C13 3.3 11.2 1 8 1 Z" fill="var(--ink)"/><circle cx="8" cy="6" r="1.9" fill="var(--brand-blue)"/></svg>
        <span>418 Wexcombe Lane<br>Brinmoor, NH 03999</span>
      </li>
    </ul>
  </section>

</main>
</body>
</html>
```